Notary Signing Agent Need Business card Design

Need a Business card design for my new company. RT Velo-Brisk LLC
Mobile Notary Signing Agent. I go to the customer for closing of Mortgage's Documents . possible signs of honesty, integrity and confidentiality.

Work with Title company to Notary Mortgage closing.

My Target Market is Title companies. Banks and Financial Institution.

Color Blue to Black Professional ) if needed some Green Little Red

And possible a company logo.

Mobile ( travel to clients ) Integrity, Honest Trustworthy. A show of Professional services.

Would like company name and my name on card

Use both sides and front with business name and my name. phone numbers.

Target Market(s)

Title company, Banks mortgage company

Industry/Entity Type

Travel

Contact Information for Business Card

Notary, Certified signing agent, Mobile

Colors
0455a3

Requirements
Must have
• Name of company , owners name phone number,
Nice to have
• blue and black color like a professional look but not limit to these only.
• a stand out from other cards .

```html
<!DOCTYPE html>
<html lang="en">
<head>
<meta charset="utf-8">
<title>RT Velo-Brisk LLC – Business Card</title>
<link href="https://fonts.googleapis.com/css2?family=Arimo:wght@700&family=Cutive+Mono&display=swap" rel="stylesheet">
<style>
  :root {
    --card-black: #252525;
    --band-blue: #2e3192;
    --edge-grey: #8a8a8a;
    --divider: #ffffff;
    --text-white: #ffffff;
    --icon-black: #111111;
  }
  * { margin: 0; padding: 0; box-sizing: border-box; }
  html, body { width: 1033px; height: 1200px; overflow: hidden; background: var(--divider); }
  .canvas { position: relative; width: 1033px; height: 1200px; background: var(--divider); }

  .card { position: absolute; left: 0; width: 1033px; background: var(--card-black); overflow: hidden; }
  .card--back { top: 0; height: 598px; border: 2px solid var(--edge-grey); }
  .card--front { top: 606px; height: 594px; }

  .band { position: absolute; background: var(--band-blue); display: flex; align-items: center;
          box-shadow: 0 0 0 1px rgba(255,255,255,0.12); }
  .band--company { left: 0; top: 95px; width: 651px; height: 140px; padding-left: 41px; }
  .band--phone { left: 545px; top: 283px; width: 488px; height: 90px; }
  .band--fax { left: 0; top: 435px; width: 630px; height: 92px; }

  .company-name { font-family: "Cutive Mono", monospace; color: var(--text-white);
                  font-size: 46px; text-decoration: underline; text-decoration-thickness: 2px;
                  text-underline-offset: 6px; white-space: nowrap; }

  .contact-number { font-family: "Arimo", sans-serif; font-weight: 700; color: var(--text-white);
                    font-size: 40px; position: absolute; white-space: nowrap; }
  .band--phone .contact-number { left: 152px; }
  .band--fax .contact-number { left: 268px; }

  .band-icon { position: absolute; }
  .band--phone .band-icon { left: 38px; top: 3px; width: 70px; height: 86px; }
  .band--fax .band-icon { left: 92px; top: 12px; width: 66px; height: 70px; }

  .front-decor { position: absolute; inset: 0; }

  .front-content { position: absolute; left: 0; right: 0; top: 220px; text-align: center; color: var(--text-white); }
  .front-content .company-name { display: inline-block; font-size: 54px; }
  .owner-name { font-family: "Cutive Mono", monospace; font-size: 68px; margin-top: 38px; white-space: nowrap; }
  .owner-phone { font-family: "Cutive Mono", monospace; font-size: 33px; margin-top: 20px; }
</style>
</head>
<body>
<div class="canvas">

  <section class="card card--back">
    <div class="band band--company">
      <span class="company-name">RT Velo-Brisk LLC.</span>
    </div>

    <div class="band band--phone">
      <svg class="band-icon" viewBox="0 0 70 86" aria-hidden="true">
        <path fill="var(--icon-black)" d="M10 6 C4 10 2 18 4 30 C8 52 22 72 40 82 C48 86 56 84 62 78 L56 64 C54 60 50 60 47 62 L42 66 C32 58 24 46 20 34 L26 30 C29 28 30 24 28 20 L22 6 C19 2 14 3 10 6 Z"/>
      </svg>
      <span class="contact-number">555-014-2290</span>
    </div>

    <div class="band band--fax">
      <svg class="band-icon" viewBox="0 0 66 70" aria-hidden="true" fill="none" stroke="var(--icon-black)" stroke-width="3">
        <rect x="14" y="3" width="38" height="20"/>
        <rect x="4" y="22" width="58" height="28" rx="3"/>
        <rect x="14" y="40" width="38" height="27"/>
        <line x1="20" y1="50" x2="46" y2="50"/>
        <line x1="20" y1="58" x2="46" y2="58"/>
        <rect x="50" y="28" width="6" height="5" fill="var(--icon-black)"/>
      </svg>
      <span class="contact-number">555-017-3318</span>
    </div>
  </section>

  <section class="card card--front">
    <svg class="front-decor" viewBox="0 0 1033 594" aria-hidden="true">
      <path fill="var(--band-blue)" d="M0 0 L300 0 C150 20 40 110 0 300 Z"/>
      <g fill="var(--band-blue)">
        <rect x="983" y="0" width="7" height="594"/>
        <rect x="996" y="0" width="7" height="594"/>
        <rect x="1010" y="0" width="7" height="594"/>
        <rect x="1024" y="0" width="9" height="594"/>
        <rect x="983" y="50" width="50" height="8"/>
        <rect x="983" y="72" width="50" height="8"/>
      </g>
      <g fill="var(--card-black)">
        <rect x="990" y="58" width="43" height="14"/>
      </g>
    </svg>

    <div class="front-content">
      <span class="company-name">RT Velo-Brisk LLC.</span>
      <p class="owner-name">Daniel R Holt</p>
      <p class="owner-phone">555-014-2290</p>
    </div>
  </section>

</div>
</body>
</html>
```